Pedicure Menu with 8 Scent Options

This design will be for a single page menu (front/back) that will display multiple different scent variations of a product. The purpose of this menu is to display to clients and show them the available options and benefits of each option.
The menu will be double sided.
The front page will include a header including brand logo and product name, and a total of 8 different scents including imagery and descriptive text.
The design should include the text provided for each scent. The design should have a layout that is structured/organized, easy to read, and has bright imagery that represents each scent.
An example is a modular layout using boxes that highlight a different scent within each box. Lavender scent should include aesthetic images of lavender flower and/or the color purple.
The back page will include brand logo, overall product description, and additional brief text that explains each step of the product.
The final size of the design should be 8.5"x11", produced in InDesign format, with all layers editable for future changes.
NOTE: Please carefully review the attached design brief that includes additional information, and all necessary text to include in the design.
Target Market(s)
Beauty/Spa Clients
Industry/Entity Type
Beauty
Requirements
Must have
- Bright and Vivid Imagery/Illustrations
Nice to have
- Background design that utilizes, lines, shapes, or other elements.

```html
<!DOCTYPE html>
<html lang="en">
<head>
<meta charset="utf-8">
<title>Velvet Ritual – Pedicure Menu</title>
<link href="https://fonts.googleapis.com/css2?family=Montserrat:wght@600;700&family=Oswald:wght@400;500&family=Sacramento&display=swap" rel="stylesheet">
<style>
:root{
  --backdrop:#262626;
  --page:#1b1b1d;
  --ink:#ffffff;
  --accent:#e8157f;
  --muted:#d9d9d9;
}
*{margin:0;padding:0;box-sizing:border-box}
html,body{width:1200px;height:1200px;overflow:hidden;background:var(--backdrop)}
.canvas{position:relative;width:1200px;height:1200px}
.page{position:absolute;top:241px;width:467px;height:732px;background:var(--page);overflow:hidden;color:var(--ink)}
.page--front{left:81px}
.page--back{left:654px}
.page__photo{position:absolute;inset:0;background:
  radial-gradient(ellipse 30% 45% at 35% 55%,rgba(70,62,60,.35),transparent 70%),
  radial-gradient(ellipse 28% 45% at 70% 50%,rgba(70,62,60,.3),transparent 70%),
  radial-gradient(ellipse 20% 30% at 5% 65%,rgba(200,190,195,.12),transparent 70%)}
.abs{position:absolute}
.wordmark{position:absolute;top:38px;left:0;width:100%;text-align:center;font-family:'Montserrat',sans-serif;font-weight:600;font-size:26px;letter-spacing:2px;color:var(--ink)}
.front-text{font-family:'Montserrat',sans-serif;font-weight:600;color:var(--ink)}
.intro{top:137px;left:43px;width:379px;font-size:8.3px;line-height:12.3px;text-align:center}
.body-para{left:36px;width:391px;font-size:8.2px;line-height:15px;text-align:justify;letter-spacing:-.1px}
.lead{top:520px;left:36px;width:391px;font-size:10.4px;line-height:18px;text-align:justify}
.lead strong{color:var(--accent)}
.contact{left:0;width:100%;text-align:center;font-family:'Oswald',sans-serif;font-size:12px;color:var(--accent);line-height:13px}
.contact svg{vertical-align:-1px;margin-right:6px}
.script{left:0;width:100%;text-align:center;font-family:'Sacramento',cursive;color:var(--accent);font-size:36px;line-height:36px}
.scent-img{position:absolute;border-radius:40%}
.scent-name{position:absolute;font-family:'Oswald',sans-serif;font-weight:500;color:var(--accent);font-size:15px;line-height:16px}
.scent-desc{position:absolute;font-family:'Oswald',sans-serif;font-size:9.6px;line-height:13px;color:var(--ink);text-transform:uppercase}
.right{text-align:right}
.steps-title{top:666px;left:0;width:100%;text-align:center;font-family:'Oswald',sans-serif;color:var(--accent);font-size:11px}
.step{position:absolute;top:694px;font-family:'Oswald',sans-serif;text-transform:uppercase}
.step b{display:block;color:var(--accent);font-weight:500;font-size:8.5px;line-height:10px}
.step span{display:block;font-size:5.2px;line-height:8px;color:var(--muted)}
.step-thumb{position:absolute;top:694px;width:35px;height:25px;border-radius:4px}
</style>
</head>
<body>
<div class="canvas">

  <section class="page page--front">
    <div class="page__photo" role="img" aria-label="Faint photo of bare feet with white orchids"></div>
    <div class="wordmark">VELVET RITUAL</div>
    <p class="abs front-text intro">LOREM IPSUM DOLOR SIT AMET, CONSECTETUER ADIPISCING ELIT. AENEAN COMMODO LIGULA EGET DOLOR. AENEAN MASSA. CUM SOCIIS NATOQUE PENATIBUS ET MAGNIS DIS PARTURIENT MONTES, NASCETUR RIDICULUS MUS. DONEC QUAM FELIS, ULTRICIES NEC, PELLENTESQUE EU, PRETIUM QUIS, SEM. NULLA CONSEQUAT MASSA QUIS ENIM. DONEC PEDE JUSTO, FRINGILLA VEL, ALIQUET NEC,</p>
    <p class="abs front-text body-para" style="top:216px">VULPUTATE EGET, ARCU. IN ENIM JUSTO, RHONCUS UT, IMPERDIET A, VENENATIS VITAE, JUSTO. NULLAM DICTUM FELIS EU PEDE MOLLIS PRETIUM. INTEGER TINCIDUNT. CRAS DAPIBUS. VIVAMUS ELEMENTUM SEMPER NISI. AENEAN VULPUTATE ELEIFEND TELLUS. AENEAN LEO LIGULA, PORTTITOR EU, CONSEQUAT VITAE, ELEIFEND AC, ENIM. ALIQUAM LOREM ANTE, DAPIBUS IN, VIVERRA QUIS, FEUGIAT A, TELLUS. PHASELLUS VIVERRA NULLA UT METUS VARIUS LAOREET. QUISQUE RUTRUM. AENEAN</p>
    <p class="abs front-text body-para" style="top:337px">IMPERDIET. ETIAM ULTRICIES NISI VEL AUGUE. CURABITUR ULLAMCORPER ULTRICIES NISI. NAM EGET DUI. ETIAM RHONCUS. MAECENAS TEMPUS, TELLUS EGET CONDIMENTUM RHONCUS, SEM QUAM SEMPER LIBERO, SIT AMET ADIPISCING SEM NEQUE SED IPSUM. NAM QUAM NUNC, BLANDIT VEL, LUCTUS PULVINAR, HENDRERIT ID, LOREM. MAECENAS NEC ODIO ET ANTE TINCIDUNT TEMPUS. DONEC</p>
    <p class="abs front-text body-para" style="top:431px">VITAE SAPIEN UT LIBERO VENENATIS FAUCIBUS. NULLAM QUIS ANTE. ETIAM SIT AMET ORCI EGET EROS FAUCIBUS TINCIDUNT. DUIS LEO. SED FRINGILLA MAURIS SIT AMET NIBH. DONEC SODALES SAGITTIS MAGNA. SED CONSEQUAT, LEO EGET BIBENDUM SODALES, AUGUE VELIT CURSUS NUNC,</p>
    <p class="abs front-text lead"><strong>VELVET RITUAL</strong> VITAE SAPIEN UT LIBERO VENENATIS FAUCIBUS. NULLAM QUIS ANTE. ETIAM SIT AMET ORCI EGET EROS FAUCIBUS TINCIDUNT. DUIS LEO. SED FRINGILLA MAURIS SIT AMET NIBH. DONEC SODALES SAGITTIS MAGNA. SED CONSEQUAT, LEO EGET BIBENDUM SODALES, AUGUE VELIT CURSUS NUNC,</p>
    <p class="abs contact" style="top:689px"><svg width="9" height="9" viewBox="0 0 10 10"><rect width="10" height="10" rx="2" fill="#e8157f"/><path d="M3 2.5c-.6.6-.4 2 .8 3.4s2.6 1.6 3.2 1l.4-.6-1.2-.9-.6.5c-.5-.2-1.3-1-1.5-1.5l.5-.6-.9-1.2z" fill="#1b1b1d"/></svg>CALL US AT : 800.555.0147</p>
    <p class="abs contact" style="top:703px"><svg width="10" height="10" viewBox="0 0 10 10"><circle cx="5" cy="5" r="4.3" fill="none" stroke="#e8157f"/><ellipse cx="5" cy="5" rx="1.8" ry="4.3" fill="none" stroke="#e8157f"/><path d="M.7 5h8.6" stroke="#e8157f"/></svg>OR TO KNOW MORE VISIT : WWW.VELVETNAILCO.COM</p>
  </section>

  <section class="page page--back">
    <div class="page__photo" role="img" aria-label="Faint photo of bare feet with white orchids"></div>
    <div class="wordmark">VELVET RITUAL</div>
    <p class="abs script" style="top:94px">pick your pedicure</p>

    <div class="scent-img" style="left:26px;top:134px;width:96px;height:44px;background:radial-gradient(circle at 50% 45%,#d6e6b4 0 28%,#f0a55a 55%,transparent 72%)" role="img" aria-label="Cucumber slices and melon wedges"></div>
    <div class="scent-name" style="left:26px;top:186px">CUCUMBER-MELON</div>
    <p class="scent-desc" style="left:26px;top:210px;width:190px">Cucumber-melon scent is a refreshing blend of crisp cucumber, watery honeydew, summer cantaloupe and sheer woods.</p>

    <div class="scent-img" style="left:352px;top:136px;width:90px;height:45px;background:radial-gradient(ellipse at 40% 55%,#8a6bc4 0 35%,#5f8a55 60%,transparent 72%)" role="img" aria-label="Lavender sprigs"></div>
    <div class="scent-name right" style="right:22px;top:188px">LAVENDER</div>
    <p class="scent-desc right" style="right:22px;top:212px;width:200px">Lavender scent provides an aroma-therapeutic relaxed session, promoting relaxation and wellness.</p>

    <div class="scent-img" style="left:23px;top:260px;width:82px;height:50px;background:radial-gradient(ellipse at 50% 45%,#5fae3a 0 40%,#2f5e22 60%,transparent 72%)" role="img" aria-label="Fresh green tea leaves"></div>
    <div class="scent-name" style="left:26px;top:318px">GREEN TEA</div>
    <p class="scent-desc" style="left:26px;top:342px;width:200px">Green tea scent is calming and relaxing,<br>leaving you refreshed and rejuvenated!</p>

    <div class="scent-img" style="left:361px;top:260px;width:81px;height:52px;background:radial-gradient(circle at 50% 50%,#ff8a1c 0 42%,#e0650a 58%,transparent 70%)" role="img" aria-label="Mandarin oranges"></div>
    <div class="scent-name right" style="right:22px;top:318px">MANDARIN</div>
    <p class="scent-desc right" style="right:22px;top:342px;width:200px">Mandarin scent is sensual and floral, uplifting the senses with a citrus blend of oils.</p>

    <div class="scent-img" style="left:25px;top:390px;width:79px;height:49px;background:radial-gradient(ellipse at 50% 50%,#4fbf4a 0 40%,#2b7a2a 58%,transparent 72%)" role="img" aria-label="Mint leaves"></div>
    <div class="scent-name" style="left:26px;top:447px">MINT</div>
    <p class="scent-desc" style="left:26px;top:471px;width:200px">Mint scent is utterly refreshing and helps to soothe inflamed skin and great to awaken the senses.</p>

    <div class="scent-img" style="left:360px;top:390px;width:84px;height:52px;background:radial-gradient(circle at 50% 50%,#d9161a 0 42%,#8e0b0f 58%,transparent 72%)" role="img" aria-label="Red roses"></div>
    <div class="scent-name right" style="right:22px;top:453px">ROSE</div>
    <p class="scent-desc right" style="right:22px;top:477px;width:200px">Rose scent is aromatic and velvety, relaxing and clearing the mind.</p>

    <div class="scent-img" style="left:184px;top:508px;width:103px;height:53px;background:radial-gradient(ellipse at 50% 50%,#f4f1e6 0 38%,#4d7d3c 58%,transparent 72%)" role="img" aria-label="White gardenia flowers"></div>
    <div class="scent-name" style="left:0;width:100%;text-align:center;top:566px">GARDENIA</div>
    <p class="scent-desc" style="left:0;width:100%;text-align:center;top:591px">Gardenia scent is sweet and delicate, leaving behind a silky,<br>floral scent that is derived from the gardenia plant.</p>

    <p class="abs script" style="top:624px">deluxe pedicure 4-step</p>
    <p class="abs steps-title">EACH BOX CONTAINS 4 ESSENTIAL STEPS:</p>

    <div class="step" style="left:29px"><b>SALT SOAK</b><span>Detoxifies and<br>deodorizes your feet.</span></div>
    <div class="step-thumb" style="left:90px;background:linear-gradient(135deg,#e8d7c8,#9bb59a)" role="img" aria-label="Feet in a salt soak"></div>
    <div class="step" style="left:137px"><b>SUGAR SCRUB</b><span>Gently exfoliates<br>dead skin.</span></div>
    <div class="step-thumb" style="left:191px;background:linear-gradient(135deg,#f3e3d6,#d9a98b)" role="img" aria-label="Sugar scrub on feet"></div>
    <div class="step" style="left:237px"><b>MUD MASK</b><span>Cleanses pores for<br>smoother skin.</span></div>
    <div class="step-thumb" style="left:296px;background:linear-gradient(135deg,#c7d8e6,#c9a27f)" role="img" aria-label="Mud mask applied to feet"></div>
    <div class="step" style="left:343px"><b>MASSAGE LOTION</b><span>Hydrates and<br>soothes skin.</span></div>
    <div class="step-thumb" style="left:402px;background:linear-gradient(135deg,#ffffff,#e6ddd8)" role="img" aria-label="Massage lotion on feet"></div>
  </section>

</div>
</body>
</html>
```